KTR Business Card

We need a new design for our business cards. We are brokers in the scrap metal industry and wants something nice, clean and very professional.

Industry/Entity Type

Business

Requirements
Must have
• Our logo
• Would probably be good to incorporate colors from logo into design.
• Example info we need on the cards.
• Name
• Company Address
• Cell Phone
• Office Phone
• Fax
• Email
• Company Website
Should not have
• Should not be too cluttered. Needs to be nice, clean and professional looking.

```html
<!DOCTYPE html>
<html lang="en">
<head>
<meta charset="utf-8">
<title>KTR Business Card</title>
<link rel="stylesheet" href="https://fonts.googleapis.com/css2?family=Source+Sans+3:wght@400;600;700&display=swap">
<style>
  :root {
    --page: #e9e6e1;
    --card-white: #ffffff;
    --brand-blue: #1f74b6;
    --brand-blue-deep: #0f5d9a;
    --brand-red: #d4202a;
    --brand-navy: #1d3563;
    --ink: #1b1b1b;
    --ink-soft: #444a52;
    --rule: #cfd6de;
  }
  * { box-sizing: border-box; margin: 0; padding: 0; }
  html, body { width: 1200px; height: 1024px; overflow: hidden; }
  body {
    background: var(--page);
    font-family: "Source Sans 3", Arial, sans-serif;
    position: relative;
  }
  .card {
    position: absolute;
    left: 280px;
    width: 640px;
    height: 366px;
    box-shadow: 0 6px 18px rgba(0,0,0,0.18);
    overflow: hidden;
  }
  .card-front { top: 96px; background: var(--card-white); }
  .card-back {
    top: 562px;
    background: linear-gradient(160deg, var(--brand-blue) 0%, var(--brand-blue-deep) 100%);
    color: #fff;
  }
  .stripes { position: absolute; inset: 0; }

  .brand {
    position: absolute;
    left: 70px;
    top: 58px;
    display: flex;
    align-items: center;
    gap: 14px;
  }
  .brand-square {
    width: 40px; height: 40px;
    background: var(--brand-blue);
  }
  .brand-name {
    font-weight: 700;
    font-size: 34px;
    color: var(--brand-navy);
    letter-spacing: 1px;
  }
  .company-name {
    position: absolute;
    left: 70px;
    top: 110px;
    font-weight: 700;
    font-size: 20px;
    color: var(--ink);
  }
  .divider {
    position: absolute;
    left: 70px;
    top: 148px;
    width: 330px;
    height: 1px;
    background: var(--rule);
  }
  .person {
    position: absolute;
    left: 70px;
    top: 160px;
    font-size: 22px;
  }
  .person-name { color: var(--brand-red); font-weight: 700; }
  .person-sep { color: var(--brand-blue); margin: 0 6px; }
  .person-title { color: var(--brand-blue); font-weight: 400; }
  .contacts {
    position: absolute;
    left: 70px;
    top: 198px;
    display: grid;
    grid-template-columns: 150px 200px;
    row-gap: 6px;
    font-size: 15px;
    color: var(--ink-soft);
  }
  .contact { display: flex; align-items: center; gap: 7px; }
  .contact svg { width: 12px; height: 12px; fill: var(--brand-blue); flex: none; }

  .back-brand {
    position: absolute;
    left: 0; right: 0;
    top: 104px;
    display: flex;
    flex-direction: column;
    align-items: center;
    gap: 14px;
  }
  .back-mark {
    display: flex; align-items: center; gap: 14px;
  }
  .back-square { width: 46px; height: 46px; background: #fff; }
  .back-brand-name { font-weight: 700; font-size: 52px; letter-spacing: 2px; }
  .back-company { font-weight: 700; font-size: 28px; }
  .back-web { font-size: 16px; opacity: 0.9; }
</style>
</head>
<body>
  <section class="card card-front" aria-label="Business card front">
    <svg class="stripes" viewBox="0 0 640 366" aria-hidden="true">
      <polygon points="250,366 640,150 640,162 272,366" fill="#1f74b6"/>
      <polygon points="284,366 640,168 640,188 320,366" fill="#d4202a"/>
      <polygon points="330,366 640,194 640,208 355,366" fill="#1d3563"/>
    </svg>
    <div class="brand">
      <span class="brand-square"></span>
      <span class="brand-name">KTR</span>
    </div>
    <div class="company-name">Keystone Trade Resources</div>
    <div class="divider"></div>
    <div class="person">
      <span class="person-name">Daniel Marsh</span><span class="person-sep">|</span><span class="person-title">Job Title</span>
    </div>
    <div class="contacts">
      <div class="contact">
        <svg viewBox="0 0 12 12"><path d="M2.5 0.5 4.5 2.5 3.4 4a6 6 0 0 0 4.6 4.6L9.5 7.5l2 2-1.5 2C5 11.5 0.5 7 0.5 2z"/></svg>
        555.214.7730
      </div>
      <div class="contact">
        <svg viewBox="0 0 12 12"><path d="M0.5 2h11v8h-11zM1.5 3v.4L6 6.6l4.5-3.2V3z"/></svg>
        info@ktrtrade.com
      </div>
      <div class="contact">
        <svg viewBox="0 0 12 12"><rect x="1" y="1" width="10" height="10" fill="none" stroke="#1f74b6" stroke-width="1.5"/></svg>
        555.214.7731
      </div>
      <div class="contact">
        <svg viewBox="0 0 12 12"><circle cx="6" cy="6" r="5.5"/></svg>
        www.ktrtrade.com
      </div>
    </div>
  </section>

  <section class="card card-back" aria-label="Business card back">
    <div class="back-brand">
      <div class="back-mark">
        <span class="back-square"></span>
        <span class="back-brand-name">KTR</span>
      </div>
      <div class="back-company">Keystone Trade Resources</div>
      <div class="back-web">www.ktrtrade.com</div>
    </div>
  </section>
</body>
</html>
```